Business card design for event company

need design double sided in square shape ( approx 6x6cm) in matt grey shades
front side :
logo ( could be in one color like picture attached ) printpress effect in a rect box

back side :
name in big font with silver foil finish ( similar to attached pic )

phone number i would like to see how it will look like if embossed ( like in credit cards )

Sample for contact on card ( will need 5 different contacts) - pls. include small icons next to each contact

KARIM SALEHI
Managing Director

+971 50 374 6619
karim@novlinkuae.com
www.novlink.ae
Building C2 , Office 318
Marsa Tirel Park

Please consider this is an urgent project . thank you in advance

```html
<!DOCTYPE html>
<html lang="en">
<head>
<meta charset="utf-8">
<title>Novlink business card</title>
<link rel="stylesheet" href="https://fonts.googleapis.com/css2?family=Montserrat:wght@200;300;400;500&display=swap">
<style>
  :root {
    --page: #d8d5d1;
    --card: #e6e6e4;
    --logo-box: #4e4442;
    --logo-text: #f4f2f0;
    --ink: #1e1e1e;
    --ink-soft: #3a3a3a;
    --foil-light: #8a8a8a;
    --foil-dark: #141414;
  }
  * { box-sizing: border-box; margin: 0; padding: 0; }
  html, body {
    width: 1200px;
    height: 998px;
    overflow: hidden;
  }
  body {
    background: var(--page);
    display: flex;
    align-items: center;
    justify-content: center;
    gap: 70px;
    font-family: "Montserrat", sans-serif;
  }
  .card {
    width: 460px;
    height: 460px;
    background: var(--card);
    position: relative;
    box-shadow: 0 2px 6px rgba(0,0,0,0.18);
  }
  .card-front {
    display: flex;
    align-items: center;
    justify-content: center;
  }
  .logo-box {
    width: 310px;
    height: 140px;
    background: var(--logo-box);
    display: flex;
    align-items: center;
    justify-content: center;
  }
  .logo-name {
    color: var(--logo-text);
    font-weight: 400;
    font-size: 50px;
    letter-spacing: 1px;
  }
  .card-back { padding: 46px 36px 0 36px; }
  .name {
    text-align: right;
    font-weight: 200;
    font-size: 66px;
    line-height: 0.82;
    letter-spacing: 1px;
    background: linear-gradient(180deg, var(--foil-light) 0%, var(--foil-dark) 45%, var(--foil-light) 70%, var(--foil-dark) 100%);
    -webkit-background-clip: text;
    background-clip: text;
    color: transparent;
  }
  .title {
    text-align: right;
    margin-top: 12px;
    font-weight: 300;
    font-size: 13px;
    letter-spacing: 9px;
    color: var(--ink-soft);
  }
  .contacts {
    list-style: none;
    margin-top: 34px;
    font-size: 14px;
    color: var(--ink);
    line-height: 1.7;
  }
  .contacts li { display: flex; align-items: center; gap: 12px; }
  .contacts li.no-icon { padding-left: 24px; }
  .contacts svg { width: 12px; height: 12px; fill: var(--ink); flex: none; }
  .phone {
    font-weight: 500;
    letter-spacing: 1px;
    text-shadow: 1px 1px 0 #ffffff, -1px -1px 0 #9a9a9a;
  }
</style>
</head>
<body>
  <section class="card card-front">
    <div class="logo-box">
      <span class="logo-name">Novlink</span>
    </div>
  </section>

  <section class="card card-back">
    <h1 class="name">KARIM<br>SALEHI</h1>
    <p class="title">MANAGING DIRECTOR</p>
    <ul class="contacts">
      <li>
        <svg viewBox="0 0 24 24" aria-hidden="true"><path d="M6.6 10.8a15 15 0 0 0 6.6 6.6l2.2-2.2c.3-.3.7-.4 1-.2 1.1.4 2.3.6 3.6.6.6 0 1 .4 1 1V20c0 .6-.4 1-1 1C10.6 21 3 13.4 3 4c0-.6.4-1 1-1h3.5c.6 0 1 .4 1 1 0 1.3.2 2.5.6 3.6.1.3 0 .7-.2 1z"/></svg>
        <span class="phone">+971 50 374 6619</span>
      </li>
      <li>
        <svg viewBox="0 0 24 24" aria-hidden="true"><path d="M2 5h20v14H2zm2 2v.5l8 5 8-5V7l-8 5z"/></svg>
        <span>karim@novlinkuae.com</span>
      </li>
      <li>
        <svg viewBox="0 0 24 24" aria-hidden="true"><path d="M12 2a10 10 0 1 0 0 20 10 10 0 0 0 0-20zm0 2c1 1.3 1.8 3 2.1 5H9.9C10.2 7 11 5.3 12 4zM4.3 11h3.5a16 16 0 0 0 0 2H4.3a8 8 0 0 1 0-2zm5.6 0h4.2a14 14 0 0 1 0 2H9.9a14 14 0 0 1 0-2zm6.3 0h3.5a8 8 0 0 1 0 2h-3.5a16 16 0 0 0 0-2zM12 20c-1-1.3-1.8-3-2.1-5h4.2c-.3 2-1.1 3.7-2.1 5z"/></svg>
        <span>www.novlink.ae</span>
      </li>
      <li>
        <svg viewBox="0 0 24 24" aria-hidden="true"><path d="M12 2a7 7 0 0 0-7 7c0 5 7 13 7 13s7-8 7-13a7 7 0 0 0-7-7zm0 9.5A2.5 2.5 0 1 1 12 6.5a2.5 2.5 0 0 1 0 5z"/></svg>
        <span>Building C2 , Office 318</span>
      </li>
      <li class="no-icon"><span>Marsa Tirel Park</span></li>
    </ul>
  </section>
</body>
</html>
```